New Architectural Firm Business Cards

New Business card to compliment previous pixel forum logo (attached). Please design a business card that is simple, modern, creative....please do not use "symbols", simply the logo and associated graphics/text. The front should contain name/address/phone/email/web address (with graphics).....back should be 100% graphic design using the logo somehow. Hoping for a two color (black and yellow) design. full bleed design, no borders

Target Market(s)

Commercial Architecture Clients

Industry/Entity Type

Architecture

Contact Information for Business Card

Please design a business card that is simple, modern, creative....please do not use "symbols", simply the logo and associated graphics/text. The front should contain name/address/phone/email/web address (with graphics).....back should be 100% graphic design using the logo somehow

Font styles to use
Sans Serif

Colors
FFF300
FFF600
FEFA6F
FFFEC7
FFFEE8

Requirements
Must have
• Clean, Modern Design
Should not have
• Stock images or "icons"

```html
<!DOCTYPE html>
<html lang="en">
<head>
<meta charset="utf-8">
<title>Norland Architecture – Business Cards</title>
<link rel="stylesheet" href="https://fonts.googleapis.com/css2?family=Archivo:wght@400;500;600&display=swap">
<style>
  :root {
    --canvas: #d3d4d6;
    --yellow: #f7c415;
    --yellow-deep: #e8b21c;
    --ink: #1d1d1b;
    --paper: #ffffff;
    --card-shadow: 0 6px 10px rgba(0, 0, 0, 0.28);
  }
  * { box-sizing: border-box; margin: 0; padding: 0; }
  html, body {
    width: 1138px;
    height: 1200px;
    overflow: hidden;
    background: var(--canvas);
    font-family: "Archivo", Arial, sans-serif;
  }
  .card-sheet {
    width: 1138px;
    height: 1200px;
    display: flex;
    flex-direction: column;
    align-items: center;
    justify-content: center;
    gap: 60px;
  }
  .card {
    width: 880px;
    height: 500px;
    border-radius: 22px;
    box-shadow: var(--card-shadow);
    position: relative;
    overflow: hidden;
  }

  /* Back: brand side */
  .card--back { background: var(--yellow); }
  .card--back .brand {
    position: absolute;
    left: 56px;
    bottom: 160px;
    display: flex;
    align-items: center;
    gap: 28px;
  }
  .card--back .brand-square {
    width: 92px;
    height: 92px;
    background: var(--yellow-deep);
    flex: none;
  }
  .card--back .brand-name {
    font-size: 72px;
    font-weight: 500;
    color: var(--ink);
    letter-spacing: 0.5px;
    line-height: 1;
  }

  /* Front: contact side */
  .card--front { background: var(--paper); }
  .card--front .brand {
    position: absolute;
    left: 112px;
    bottom: 118px;
    width: 290px;
    font-size: 30px;
    font-weight: 500;
    color: var(--ink);
    line-height: 1.15;
    white-space: nowrap;
  }
  .divider span {
    position: absolute;
    left: 440px;
    width: 3px;
    background: var(--ink);
  }
  .divider .divider-top { top: 125px; height: 40px; }
  .divider .divider-accent { top: 172px; height: 156px; width: 5px; left: 439px; background: var(--yellow); }
  .divider .divider-bottom { top: 334px; height: 42px; }
  .contact {
    position: absolute;
    left: 503px;
    top: 128px;
    color: var(--ink);
    font-size: 17px;
    font-weight: 500;
    letter-spacing: 0.8px;
    line-height: 17px;
    white-space: nowrap;
  }
  .contact-name {
    font-size: 28px;
    line-height: 28px;
    font-weight: 400;
    color: var(--yellow);
    letter-spacing: 0.5px;
  }
  .contact-role { margin-top: 12px; }
  .contact-phone { margin-top: 22px; }
  .contact-email { margin-top: 17px; }
  .contact-web { margin-top: 18px; }
  .contact-address { margin-top: 36px; line-height: 26px; }
</style>
</head>
<body>
  <main class="card-sheet">
    <section class="card card--back" aria-label="Card back">
      <div class="brand">
        <span class="brand-square"></span>
        <span class="brand-name">NORLAND ARCHITECTURE</span>
      </div>
    </section>

    <section class="card card--front" aria-label="Card front">
      <div class="brand">NORLAND<br>ARCHITECTURE</div>
      <div class="divider" aria-hidden="true">
        <span class="divider-top"></span>
        <span class="divider-accent"></span>
        <span class="divider-bottom"></span>
      </div>
      <div class="contact">
        <p class="contact-name">DANIEL FERRATO</p>
        <p class="contact-role">C.E.O</p>
        <p class="contact-phone">555-014-2290</p>
        <p class="contact-email">hello@norlandarch.com</p>
        <p class="contact-web">www.norlandarch.com</p>
        <p class="contact-address">1450 Ridgeline Rd<br>Cedar Hollow, GA 30999</p>
      </div>
    </section>
  </main>
</body>
</html>
```